Flyer needed for intellectual science & religion seminar

Hello! We need a 4 x 6 flier designed for an intellectual seminar on science and its compatibility with religion.

Details below:

FRONT of flyer:

The Quiet Orbit

Nov 21, 2015
10 am - 7 pm

Marlowe Banquet Hall
1187 Fenwick Blvd,
Santa Clara, CA 95081

Seating is Limited! Register Now!
www.VarentaForum.example

BACK of flyer:

"Are science and Islam compatible? Do we still need God to explain our universe? In this course we will seek the answers to such questions in the universe itself and discover that the revelation is a special lens through which we can see the truth underlying the reality. We will also zoom in to a few key areas in science such as evolution, the big bang and neuroscience."

Some Topics to be Covered:
- Destiny & quantum mechanics
- Intelligent design & evolution
- Soul searching & artificial intelligence

Register Now!
www.VarentaForum.example
info@varentaforum.example
1-877-Varenta

Target Market(s)

College students, young professionals, intellectually inclined community members.

Requirements
Must have
• A man looking through a telescope, out at the universe/cosmos. He must have a quill pen and book next to him, as if he were studying. Flyer must also incorporate an astrolabe in the images/designs used. Thank you!

```html
<!DOCTYPE html>
<html lang="en">
<head>
<meta charset="UTF-8">
<title>The Quiet Orbit — Seminar Flyer</title>
<link rel="stylesheet" href="https://fonts.googleapis.com/css2?family=Comfortaa:wght@300;400&family=Open+Sans:wght@400;600;700&display=swap">
<style>
  :root {
    --paper: #ffffff;
    --ink: #2b2b2b;
    --slate: #3b4c5e;
    --slate-dark: #2c3b4b;
    --band: rgba(118, 122, 126, 0.78);
    --photo-deep: #140d08;
    --photo-shelf: #2e2a24;
    --photo-mid: #5a3b22;
    --photo-warm: #b07a44;
    --photo-gold: #d9b27a;
    --photo-rust: #7a3e1c;
    --white: #ffffff;
  }
  html, body {
    margin: 0;
    padding: 0;
    width: 800px;
    height: 1200px;
    overflow: hidden;
    background: var(--paper);
  }
  .flyer {
    position: relative;
    width: 800px;
    height: 1200px;
    background: var(--paper);
    font-family: "Open Sans", Arial, sans-serif;
    color: var(--ink);
    overflow: hidden;
  }
  .hero-photo {
    position: absolute;
    left: 0;
    top: 0;
    width: 800px;
    height: 597px;
    background:
      radial-gradient(ellipse 22% 18% at 60% 72%, rgba(217,178,122,0.85) 0%, rgba(217,178,122,0) 100%),
      radial-gradient(ellipse 16% 20% at 53% 26%, rgba(200,170,130,0.7) 0%, rgba(200,170,130,0) 100%),
      radial-gradient(ellipse 34% 42% at 45% 55%, rgba(176,122,68,0.9) 0%, rgba(176,122,68,0) 100%),
      radial-gradient(ellipse 30% 35% at 30% 70%, rgba(122,62,28,0.75) 0%, rgba(122,62,28,0) 100%),
      radial-gradient(ellipse 28% 40% at 88% 35%, rgba(120,90,60,0.55) 0%, rgba(120,90,60,0) 100%),
      radial-gradient(ellipse 40% 30% at 35% 10%, rgba(90,80,64,0.7) 0%, rgba(90,80,64,0) 100%),
      linear-gradient(100deg, var(--photo-shelf) 0%, var(--photo-mid) 45%, var(--photo-deep) 100%);
  }
  .title-band {
    position: absolute;
    left: 0;
    top: 497px;
    width: 750px;
    height: 100px;
    background: var(--band);
  }
  .title {
    position: absolute;
    left: 26px;
    top: 508px;
    margin: 0;
    font-family: "Comfortaa", "Century Gothic", sans-serif;
    font-weight: 300;
    font-size: 55px;
    letter-spacing: 1px;
    color: var(--white);
  }
  .title-rule {
    position: absolute;
    left: 26px;
    top: 576px;
    width: 724px;
    height: 3px;
    background: var(--white);
  }
  .brand {
    position: absolute;
    left: 30px;
    top: 680px;
  }
  .brand-name {
    font-weight: 600;
    font-size: 34px;
    color: var(--slate);
    line-height: 1;
    display: flex;
    align-items: center;
    gap: 10px;
  }
  .brand-dot {
    width: 16px;
    height: 16px;
    border-radius: 50%;
    background: var(--slate);
  }
  .brand-tagline {
    margin-top: 8px;
    font-size: 11px;
    letter-spacing: 0.5px;
    color: var(--slate);
  }
  .date-box {
    position: absolute;
    left: 389px;
    top: 673px;
    width: 411px;
    height: 70px;
    background: var(--slate);
    color: var(--white);
    font-weight: 700;
    font-size: 27px;
    display: flex;
    align-items: center;
    justify-content: center;
  }
  .venue {
    position: absolute;
    left: 458px;
    top: 818px;
    margin: 0;
    font-style: normal;
    font-size: 24px;
    line-height: 34px;
    color: var(--ink);
  }
  .register-button {
    position: absolute;
    left: 153px;
    top: 1005px;
    width: 537px;
    height: 52px;
    background: var(--slate-dark);
    outline: 2px solid var(--slate-dark);
    outline-offset: 3px;
    color: var(--white);
    font-weight: 700;
    font-size: 25px;
    display: flex;
    align-items: center;
    justify-content: center;
  }
  .website {
    position: absolute;
    left: 0;
    top: 1082px;
    width: 800px;
    text-align: center;
    font-weight: 600;
    font-size: 18px;
    letter-spacing: 3px;
    color: var(--ink);
  }
</style>
</head>
<body>
  <main class="flyer">
    <div class="hero-photo" role="img" aria-label="Scholar in robes and turban writing with a quill in a candlelit study, with bookshelves, a brass telescope and an astrolabe"></div>

    <div class="title-band"></div>
    <h1 class="title">The Quiet Orbit</h1>
    <div class="title-rule"></div>

    <div class="brand">
      <div class="brand-name"><span class="brand-dot"></span>Varenta Forum</div>
      <div class="brand-tagline">Think Deeply | Ask Boldly</div>
    </div>

    <div class="date-box">Nov 21, 2015 | 10 am - 7 pm</div>

    <address class="venue">
      Marlowe Banquet Hall<br>
      1187 Fenwick Blvd,<br>
      Santa Clara, CA 95081
    </address>

    <div class="register-button">Seating is Limited! Register Now!</div>

    <div class="website">www.VarentaForum.example</div>
  </main>
</body>
</html>
```